Assessment Report cover design and formatting

This report is for senior executives and provides leaders with detailed insight into their capabilities and skills. The cover should have space for the date and name of the person doing the assessment. We are looking to modernise the report cover design. We would like the report to be our company colours if possible. The work will likely expand once the cover is done to other parts of the report, ie. the format and layout of the report etc.

Company colours:
Primary colours:
• Blue #0D47A1, #115CD0, #90B6ED, #EEf3FB
• Green #0D91A1, #47A10D, #324C196, #0DA11D
Additional colours:
• Purple #A10D91
• Brown #A1670D
• Red #A10D47

Target Market(s)

Executives

Industry/Entity Type

Consulting, leadership development

Colors
0094D4
00A9DD
6FCCEA
C7EBF8
E9F6FB
00AB8E
00BBA5
67D7C9
C6EFE9
E9F9F6
E54698
E96AAD
F1A4CE
F9D9EA
FCEFF6
6B429C
8869AF
B7A5CE
E3DAEB
F3F0F8

Requirements
Must have
• The report cover should have space for name of user, the date and company logo. Cover should be in A4 size.

```html
<!DOCTYPE html>
<html lang="en">
<head>
<meta charset="utf-8">
<title>Growth Leader Assessment – Report Cover</title>
<link rel="stylesheet" href="https://fonts.googleapis.com/css2?family=Montserrat:wght@400;800&family=Bebas+Neue&family=Fira+Sans:wght@400&display=swap">
<style>
  :root {
    --page-bg: #e6e9ee;
    --ink-dark: #1d2226;
    --ink-dark-2: #2e3439;
    --photo-low-1: #3a4550;
    --photo-low-2: #26303a;
    --green: #10a11d;
    --green-bright: #47c40d;
    --teal: #0a9488;
    --blue: #115cd0;
    --blue-deep: #0d3fa8;
    --blue-sky: #0a6fd0;
    --white: #ffffff;
  }
  * { margin: 0; padding: 0; box-sizing: border-box; }
  html, body {
    width: 1200px; height: 719px; overflow: hidden;
    background: var(--page-bg);
  }
  .cover {
    position: absolute; left: 359px; top: 20px;
    width: 481px; height: 680px; overflow: hidden;
    box-shadow: 0 6px 24px rgba(0,0,0,.35);
    background: var(--photo-low-2);
  }
  .cover-art { position: absolute; inset: 0; width: 481px; height: 680px; }
  .title { position: absolute; left: 199px; top: 78px; width: 260px; }
  .title-growth {
    font-family: "Montserrat", sans-serif; font-weight: 400;
    font-size: 56px; line-height: 1; color: var(--white); letter-spacing: -1px;
    padding-left: 8px;
  }
  .title-leader {
    font-family: "Montserrat", sans-serif; font-weight: 800;
    font-size: 52px; line-height: 1; color: var(--green);
    margin-top: 2px; padding-left: 10px; letter-spacing: 1px;
  }
  .title-assessment {
    display: inline-block; margin-top: 6px;
    background: linear-gradient(90deg, var(--blue) 0%, var(--blue) 75%, rgba(17,92,208,0) 100%);
    font-family: "Bebas Neue", sans-serif; font-size: 58px; line-height: 68px;
    color: var(--white); padding: 2px 22px 0 14px; letter-spacing: 0.5px;
  }
  .report-tag {
    position: absolute; left: 51px; top: 420px; width: 192px; height: 39px;
    background: linear-gradient(90deg, var(--green) 0%, var(--green) 70%, rgba(16,161,29,0) 100%);
    font-family: "Bebas Neue", sans-serif; font-size: 27px; line-height: 41px;
    color: var(--white); padding-left: 9px; letter-spacing: 0.3px;
  }
  .report-date { position: absolute; left: 90px; top: 462px; }
  .brand {
    position: absolute; left: 292px; top: 560px; width: 170px;
    color: var(--white); font-family: "Fira Sans", sans-serif; font-weight: 400;
    text-align: left;
  }
  .brand-name { font-size: 23px; line-height: 1.2; letter-spacing: 2px; display: flex; align-items: center; gap: 8px; }
  .brand-mark { width: 10px; height: 10px; border-radius: 50%; background: var(--white); flex: none; }
  .brand-tagline { font-size: 11px; letter-spacing: 2.4px; margin-top: 6px; }
</style>
</head>
<body>
  <main class="cover">
    <svg class="cover-art" viewBox="0 0 481 680" xmlns="http://www.w3.org/2000/svg">
      <defs>
        <linearGradient id="photoLow" x1="0" y1="0" x2="1" y2="1">
          <stop offset="0" stop-color="var(--photo-low-1)"/>
          <stop offset="1" stop-color="var(--photo-low-2)"/>
        </linearGradient>
        <linearGradient id="photoTop" x1="0" y1="0" x2="0" y2="1">
          <stop offset="0" stop-color="var(--ink-dark)"/>
          <stop offset="1" stop-color="var(--ink-dark-2)"/>
        </linearGradient>
        <linearGradient id="swoosh" x1="0" y1="0" x2="1" y2="0">
          <stop offset="0" stop-color="var(--green)"/>
          <stop offset="0.55" stop-color="var(--teal)"/>
          <stop offset="1" stop-color="var(--blue-sky)"/>
        </linearGradient>
        <linearGradient id="corner" x1="0" y1="0" x2="0" y2="1">
          <stop offset="0" stop-color="var(--teal)"/>
          <stop offset="1" stop-color="var(--blue-sky)"/>
        </linearGradient>
        <linearGradient id="yearFill" x1="0" y1="0" x2="0" y2="1">
          <stop offset="0" stop-color="var(--green-bright)"/>
          <stop offset="1" stop-color="var(--blue)"/>
        </linearGradient>
      </defs>

      <rect x="0" y="0" width="481" height="680" fill="url(#photoLow)" role="img" aria-label="Photo of executives in a meeting in a bright office"/>
      <path d="M0 0 H481 V362 C380 420 190 460 0 300 Z" fill="var(--white)"/>
      <path d="M0 0 H481 V356 C370 410 170 420 0 254 Z" fill="url(#swoosh)"/>
      <path d="M0 0 H481 V350 C360 405 140 380 0 144 Z" fill="url(#photoTop)" role="img" aria-label="Dark abstract architectural background"/>

      <path d="M165 680 C190 560 300 470 481 452 V680 Z" fill="var(--white)"/>
      <path d="M180 680 C205 565 310 478 481 460 V680 Z" fill="var(--blue-deep)"/>
      <path d="M205 680 C232 575 330 500 481 482 V680 Z" fill="url(#corner)"/>

      <text x="112" y="538" transform="rotate(-90 112 538)" font-family="Montserrat, sans-serif" font-weight="800" font-size="26" fill="var(--green-bright)">AUG</text>
      <text x="118" y="531" font-family="'Bebas Neue', sans-serif" font-size="88" fill="url(#yearFill)" stroke="var(--white)" stroke-width="2.5" paint-order="stroke" letter-spacing="1">2023</text>
    </svg>

    <div class="title">
      <div class="title-growth">Growth</div>
      <div class="title-leader">LEADER</div>
      <div class="title-assessment">ASSESSMENT</div>
    </div>

    <div class="report-tag">INSIGHT REPORT FOR</div>

    <div class="brand">
      <div class="brand-name"><span class="brand-mark"></span>Meridian Partners</div>
      <div class="brand-tagline">Builders of Leaders</div>
    </div>
  </main>
</body>
</html>
```